Business Card Re-Design/Update

We'd like to update out business cards. I've included our current "Style guide" which has the colour scheme of the organisation in it. I've also included the branding files with logos etc in them.

I've also included a copy of one of our existing cards so that you can see how ugly/dated they look. I'd like a fresh modern corporate look.

Target Market(s)

These are for our clients, potential clients, industry contacts - like all business cards

Contact Information for Business Card

Name
Position
Company Address - Level 1, 47 Garnet Lane, Toowong Qld 4066
Direct Phone
mobile
Email
Website -www.korvalnet.com.au
Logo

Colors

Designer to choose colors to be used in the design.

Requirements
Must have
• Main Logo
• Cards will need to be editable to be able to personalize them for each new employee.
Nice to have
• The MapOUT, HandOVER, UpKEEP would be okay to have if they can be sensibly and professionally added to the look without detracting from the main imagery.
• Maybe they could go on the back of the card? will leave this to your creative discretion as to whether/where they fit.
Should not have
• Should not have decorative or script fonts

```html
<!DOCTYPE html>
<html lang="en">
<head>
<meta charset="utf-8">
<title>korvalnet business cards</title>
<link rel="stylesheet" href="https://fonts.googleapis.com/css2?family=Lato:wght@400;700;900&family=Oswald:wght@500&display=swap">
<style>
  :root {
    --backdrop: #262626;
    --brand-red: #d8121b;
    --brand-red-deep: #b80d14;
    --ink: #2f2f2f;
    --ink-soft: #555555;
    --paper: #fafafa;
    --rule: #9a9a9a;
  }
  * { margin: 0; padding: 0; box-sizing: border-box; }
  html, body { width: 1200px; height: 997px; overflow: hidden; }
  body {
    background: var(--backdrop);
    font-family: "Lato", Arial, sans-serif;
    position: relative;
  }
  .card {
    position: absolute;
    width: 600px;
    height: 343px;
    border-radius: 3px;
    box-shadow: 0 12px 30px rgba(0,0,0,0.55);
    overflow: hidden;
  }

  /* Back of card */
  .card-back {
    left: 110px;
    top: 100px;
    background: radial-gradient(ellipse at 50% 40%, var(--brand-red) 0%, var(--brand-red-deep) 100%);
    color: #ffffff;
  }
  .card-back .wordmark {
    position: absolute;
    left: 0; right: 0; top: 118px;
    display: flex;
    justify-content: center;
    align-items: center;
    gap: 14px;
    font-size: 54px;
    font-weight: 700;
    letter-spacing: -0.5px;
    color: #ffffff;
  }
  .card-back .wordmark-square {
    width: 30px; height: 30px;
    background: #ffffff;
  }
  .card-back .website {
    position: absolute;
    left: 0; right: 0; bottom: 56px;
    text-align: center;
    font-size: 15px;
    font-weight: 700;
    letter-spacing: 6px;
    text-transform: uppercase;
    color: rgba(255,255,255,0.9);
  }

  /* Front of card */
  .card-front {
    left: 490px;
    top: 500px;
    background: var(--paper);
    color: var(--ink);
  }
  .card-front .wordmark {
    position: absolute;
    left: 46px; top: 52px;
    display: flex;
    align-items: center;
    gap: 12px;
    font-size: 44px;
    font-weight: 700;
    letter-spacing: -0.5px;
    color: var(--ink);
  }
  .card-front .wordmark-square {
    width: 26px; height: 26px;
    background: var(--brand-red);
  }
  .person {
    position: absolute;
    left: 46px; top: 176px;
    width: 230px;
    text-align: right;
  }
  .person-name {
    font-family: "Oswald", "Arial Narrow", sans-serif;
    font-weight: 500;
    font-size: 20px;
    letter-spacing: 0.5px;
    color: var(--brand-red);
    text-transform: uppercase;
    line-height: 1.1;
  }
  .person-role {
    font-size: 14px;
    color: var(--ink-soft);
    margin-top: 2px;
  }
  .divider {
    position: absolute;
    left: 296px; top: 138px;
    width: 2px; height: 112px;
    background: linear-gradient(to bottom, rgba(0,0,0,0), var(--rule) 40%, var(--rule) 60%, rgba(0,0,0,0));
  }
  .contact-list {
    position: absolute;
    left: 320px; top: 134px;
    list-style: none;
  }
  .contact-list li {
    display: flex;
    align-items: center;
    gap: 10px;
    height: 28px;
    font-size: 15px;
    color: var(--ink);
  }
  .contact-list .note { font-size: 12px; color: var(--ink-soft); margin-left: 4px; }
  .contact-icon { width: 20px; height: 20px; flex: none; }
  .address-band {
    position: absolute;
    left: 0; right: 0; bottom: 0;
    height: 52px;
    background: var(--brand-red);
    color: #ffffff;
    font-weight: 700;
    font-size: 16px;
    display: flex;
    align-items: center;
    justify-content: center;
    letter-spacing: 0.3px;
  }
</style>
</head>
<body>

<section class="card card-back" aria-label="Card back">
  <div class="wordmark"><span class="wordmark-square"></span><span>korvalnet</span></div>
  <div class="website">www.korvalnet.com.au</div>
</section>

<section class="card card-front" aria-label="Card front">
  <div class="wordmark"><span class="wordmark-square"></span><span>korvalnet</span></div>

  <div class="person">
    <div class="person-name">Dana Whitford</div>
    <div class="person-role">Business Development Manager</div>
  </div>

  <div class="divider"></div>

  <ul class="contact-list">
    <li>
      <svg class="contact-icon" viewBox="0 0 20 20" aria-hidden="true"><circle cx="10" cy="10" r="10" fill="#d8121b"/><path d="M6.5 5.5h2l1 2.5-1.3 1a6 6 0 0 0 2.8 2.8l1-1.3 2.5 1v2a1 1 0 0 1-1 1A8.5 8.5 0 0 1 5.5 6.5a1 1 0 0 1 1-1z" fill="#fff"/></svg>
      <span>+61 (0)400 555 018</span>
    </li>
    <li>
      <svg class="contact-icon" viewBox="0 0 20 20" aria-hidden="true"><circle cx="10" cy="10" r="10" fill="#d8121b"/><rect x="5" y="8" width="10" height="6" rx="1" fill="#fff"/><rect x="7" y="5" width="6" height="3" fill="#fff"/><rect x="7" y="10" width="6" height="1.2" fill="#d8121b"/></svg>
      <span>+61 (0)7 3000 4120</span>
    </li>
    <li>
      <svg class="contact-icon" viewBox="0 0 20 20" aria-hidden="true"><circle cx="10" cy="10" r="10" fill="#d8121b"/><path d="M6.5 5.5h2l1 2.5-1.3 1a6 6 0 0 0 2.8 2.8l1-1.3 2.5 1v2a1 1 0 0 1-1 1A8.5 8.5 0 0 1 5.5 6.5a1 1 0 0 1 1-1z" fill="#fff"/></svg>
      <span>+61 (0)7 3000 4127<span class="note">(Direct)</span></span>
    </li>
    <li>
      <svg class="contact-icon" viewBox="0 0 20 20" aria-hidden="true"><circle cx="10" cy="10" r="10" fill="#d8121b"/><rect x="5" y="6.5" width="10" height="7" rx="1" fill="#fff"/><path d="M5.5 7l4.5 3.5L14.5 7" fill="none" stroke="#d8121b" stroke-width="1.2"/></svg>
      <span>dwhitford@korvalnet.com.au</span>
    </li>
  </ul>

  <div class="address-band">Level 1, 47 Garnet Lane, Toowong Qld 4066</div>
</section>

</body>
</html>
```